Letterhead and Envelope Design for Investment Company

We need a letterhead and envelope design.
We are a family owned investment company doing direct investments into other family owned businesses.
I have attached all our current marketing material including our logo for reference.

Our under construction website can be found here:
https://rob-darke-qv7m.pagevorlo.com/
password: Copperfen

Target Market(s)

Bankers, business owners, financial partners

Industry/Entity Type

Investment

Colors

Designer to choose colors to be used in the design.

Requirements
Must have
• Logo, and company information

```html
<!DOCTYPE html>
<html lang="en">
<head>
<meta charset="utf-8">
<title>Copperfen Holdings Stationery</title>
<link href="https://fonts.googleapis.com/css2?family=Open+Sans:wght@400;600;700&display=swap" rel="stylesheet">
<style>
:root{
  --bg:#e7e7e5;
  --paper:#ffffff;
  --ink:#1a1a1a;
  --black:#151515;
  --gold:#e0ac2a;
  --gold-deep:#c99320;
  --muted:#555555;
  --white:#ffffff;
}
*{box-sizing:border-box;margin:0;padding:0}
html,body{width:1200px;height:900px;overflow:hidden;background:var(--bg);font-family:"Open Sans",sans-serif;color:var(--ink)}
.canvas{position:relative;width:1200px;height:900px}
.sheet{position:absolute;background:var(--paper);box-shadow:0 2px 6px rgba(0,0,0,.12);overflow:hidden}

.brand{display:flex;align-items:center;gap:6px;font-weight:600;letter-spacing:.08em;text-transform:uppercase;color:var(--ink);white-space:nowrap}
.brand-dot{width:8px;height:8px;border-radius:50%;background:var(--gold);flex:none}
.brand.on-dark{color:var(--white)}

.contact{font-size:7px;line-height:1.7;color:var(--muted)}
.contact li{list-style:none;display:flex;align-items:center;gap:4px;white-space:nowrap}
.contact .ico{width:7px;height:7px;background:var(--gold);display:inline-block;flex:none}

/* letterhead */
.letterhead{left:60px;top:100px;width:480px;height:690px}
.letterhead .brand{position:absolute;left:38px;top:44px;font-size:15px}
.letterhead .contact{position:absolute;right:36px;top:38px}
.footer-bands{position:absolute;left:0;right:0;bottom:0;height:34px}
.band-black{position:absolute;left:0;bottom:0;width:46%;height:14px;background:var(--black)}
.band-gold{position:absolute;right:0;bottom:0;width:54%;height:22px;background:var(--gold-deep)}

/* envelope front */
.envelope-front{left:600px;top:80px;width:540px;height:250px}
.envelope-front .brand{position:absolute;right:30px;top:30px;font-size:12px}
.envelope-front .contact{position:absolute;left:24px;bottom:28px;font-size:6px}
.envelope-front .band-gold{background:var(--gold);height:16px}
.envelope-front .band-black{height:9px}

/* envelope back */
.envelope-back{left:600px;top:360px;width:540px;height:250px;background:var(--black)}
.envelope-back .flap{position:absolute;left:0;top:0;width:540px;height:110px}
.envelope-back .brand{position:absolute;left:50%;top:42px;transform:translateX(-50%);font-size:14px}
.envelope-back .url{position:absolute;left:0;right:0;bottom:24px;text-align:center;font-size:9px;color:var(--white);letter-spacing:.05em}

/* business cards */
.card{width:255px;height:150px;top:660px}
.card-back{left:600px;background:var(--black)}
.card-back .brand{position:absolute;left:50%;top:52px;transform:translateX(-50%);font-size:11px}
.card-back .rule{position:absolute;left:50px;right:50px;top:76px;height:1px;background:var(--gold)}
.card-back .url{position:absolute;left:0;right:0;top:88px;text-align:center;font-size:7px;color:var(--white);letter-spacing:.05em}

.card-front{left:885px}
.card-front .brand{position:absolute;left:12px;top:69px;font-size:7.5px;gap:5px}
.card-front .brand-dot{width:7px;height:7px}
.card-front .person{position:absolute;left:128px;right:10px;top:30px;border-left:1px solid #ddd;padding-left:8px}
.card-front .name{font-size:10px;font-weight:700;color:var(--gold-deep)}
.card-front .role{font-size:7px;margin-bottom:6px}
.card-front .contact{font-size:6px}
</style>
</head>
<body>
<main class="canvas">

  <section class="sheet letterhead">
    <div class="brand"><span class="brand-dot"></span>Copperfen Holdings Inc</div>
    <ul class="contact">
      <li>48 Linden Ave, Suite 210</li>
      <li>Marlow Falls, IA 50999</li>
      <li><span class="ico"></span>555-014-2270</li>
      <li><span class="ico"></span>hello@copperfenholdings.com</li>
      <li><span class="ico"></span>www.copperfenholdings.com</li>
    </ul>
    <div class="footer-bands"><div class="band-black"></div><div class="band-gold"></div></div>
  </section>

  <section class="sheet envelope-front">
    <div class="brand"><span class="brand-dot"></span>Copperfen Holdings Inc</div>
    <ul class="contact">
      <li>48 Linden Ave, Suite 210</li>
      <li>Marlow Falls, IA 50999</li>
      <li><span class="ico"></span>555-014-2270</li>
      <li><span class="ico"></span>hello@copperfenholdings.com</li>
      <li><span class="ico"></span>www.copperfenholdings.com</li>
    </ul>
    <div class="footer-bands"><div class="band-black"></div><div class="band-gold"></div></div>
  </section>

  <section class="sheet envelope-back">
    <svg class="flap" viewBox="0 0 540 110" aria-hidden="true">
      <path d="M0 0 H540 V60 Q540 78 520 80 L30 106 Q0 108 0 85 Z" fill="#ffffff"/>
    </svg>
    <div class="brand"><span class="brand-dot"></span>Copperfen Holdings Inc</div>
    <p class="url">www.copperfenholdings.com</p>
  </section>

  <section class="sheet card card-back">
    <div class="brand on-dark"><span class="brand-dot"></span>Copperfen Holdings Inc</div>
    <div class="rule"></div>
    <p class="url">www.copperfenholdings.com</p>
  </section>

  <section class="sheet card card-front">
    <div class="brand"><span class="brand-dot"></span>Copperfen Holdings</div>
    <div class="person">
      <p class="name">Nora Pell</p>
      <p class="role">Vice President</p>
      <ul class="contact">
        <li>48 Linden Ave, Suite 210</li>
        <li>Marlow Falls, IA 50999</li>
        <li><span class="ico"></span>555-014-2270</li>
        <li><span class="ico"></span>nora@copperfenholdings.com</li>
        <li><span class="ico"></span>www.copperfenholdings.com</li>
      </ul>
    </div>
  </section>

</main>
</body>
</html>
```